Warren D Pellham New Business Card Design

I assist families or individuals with downsizing. When they need to sell estate items I manage the process. I may buy their items. I may place their items with auction houses or I may bring in a variety of experts to sell all of the items. We help clients sell a huge variety of items including art, jewelry, coins, watches, antiques, collectibles, etc.

Target Market(s)

Two markets...One market is the clients I serve which are usually seniors or their family. These are individuals that need to sell on item or a house full if they estate is being liquidated. The other market is those that refer clients to me. Real Estate professionals, active senior communities, trust and estate lawyers and financial advisors.

Contact Information for Business Card

This is a new business so we do not have a logo. We may not need a logo. Feel free to visit our website at www.warrendpellham-example.com for more information on the service we provide. I am a private consultant so my name needs to be prominent. My name is my brand. We need the card to let people know how to contact us via phone, website and email. Easy to read. Many of our clients are elderly.

Font styles to use
Sans Serif

Requirements
Must have
• My name. Our contact information.
• Warren D Pellham
• 555-218-7034 Office
• 555-639-1582 Cell
• info@warrendpellham-example.com
• www.warrendpellham-example.com

```html
<!DOCTYPE html>
<html lang="en">
<head>
<meta charset="utf-8">
<title>Warren D Pellham – Business Card</title>
<link rel="stylesheet" href="https://fonts.googleapis.com/css2?family=Bebas+Neue&family=Oswald:wght@600;700&family=Montserrat:wght@400;500&display=swap">
<style>
  :root {
    --bg: #e9e6e1;
    --card-dark: #3b3129;
    --card-tan: #c3ae91;
    --ink-dark: #3a2f27;
    --ink-soft: #5a4b3e;
    --ink-tan: #cbb89c;
    --photo-top: #d9d4cc;
    --photo-bottom: #4a4a50;
  }
  * { box-sizing: border-box; margin: 0; padding: 0; }
  html, body { width: 1200px; height: 900px; overflow: hidden; }
  body {
    background: var(--bg);
    position: relative;
  }
  .card {
    position: absolute;
    left: 320px;
    width: 560px;
    height: 320px;
    border-radius: 22px;
    box-shadow: 0 10px 28px rgba(0,0,0,0.18);
    overflow: hidden;
  }
  /* Back side */
  .card-back {
    top: 105px;
    background: var(--card-dark);
    display: flex;
    align-items: center;
    justify-content: center;
  }
  .card-back .name {
    font-family: "Bebas Neue", "Oswald", sans-serif;
    font-size: 66px;
    letter-spacing: 1px;
    color: var(--ink-tan);
  }
  /* Front side */
  .card-front {
    top: 475px;
    background: var(--card-tan);
  }
  .portrait {
    position: absolute;
    left: 345px;
    top: 40px;
    width: 175px;
    height: 180px;
    background: linear-gradient(180deg, var(--photo-top) 0%, #b7aa9c 45%, var(--photo-bottom) 100%);
  }
  .name-block {
    position: absolute;
    left: 0;
    top: 128px;
    display: flex;
    align-items: stretch;
  }
  .name-bar {
    width: 34px;
    background: var(--card-dark);
    margin-right: 16px;
  }
  .name-block .name {
    font-family: "Bebas Neue", "Oswald", sans-serif;
    font-size: 42px;
    line-height: 0.95;
    color: var(--ink-dark);
    letter-spacing: 0.5px;
  }
  .tagline {
    font-family: "Oswald", sans-serif;
    font-weight: 700;
    font-size: 10.5px;
    letter-spacing: 0.3px;
    text-transform: uppercase;
    color: var(--ink-dark);
    margin-top: 2px;
  }
  .contact-list {
    position: absolute;
    left: 50px;
    top: 218px;
    list-style: none;
    font-family: "Montserrat", sans-serif;
    font-size: 15px;
    color: var(--ink-dark);
  }
  .contact-list li {
    display: flex;
    align-items: center;
    gap: 14px;
    height: 28px;
    white-space: nowrap;
  }
  .contact-list svg { width: 16px; height: 16px; fill: var(--ink-dark); flex: none; }
  .phone-label {
    font-size: 12px;
    color: var(--ink-soft);
    margin-left: 4px;
  }
  .phone-sep {
    margin: 0 8px;
    color: var(--ink-soft);
  }
</style>
</head>
<body>

  <section class="card card-back">
    <div class="name">Warren D Pellham</div>
  </section>

  <section class="card card-front">
    <div class="portrait" role="img" aria-label="Portrait photograph of Warren D Pellham in a dark suit and tie"></div>

    <div class="name-block">
      <div class="name-bar"></div>
      <div>
        <div class="name">Warren D Pellham</div>
        <div class="tagline">Collectable Asset Buyer, Broker &amp; Consultant</div>
      </div>
    </div>

    <ul class="contact-list">
      <li>
        <svg viewBox="0 0 16 16" aria-hidden="true"><path d="M1 5c0-2 3-3 7-3s7 1 7 3v1.5h-3.5V5c-1-.6-2.2-.8-3.5-.8S5.5 4.4 4.5 5v1.5H1z"/><path d="M4 8l1.5-2h5L12 8l2 4.5v1.5H2v-1.5z"/><circle cx="8" cy="10.5" r="1.6" fill="#c3ae91"/></svg>
        <span>555-218-7034<span class="phone-label">Office</span><span class="phone-sep">|</span>555-639-1582<span class="phone-label">Cell</span></span>
      </li>
      <li>
        <svg viewBox="0 0 16 16" aria-hidden="true"><path d="M15 1L1 7l5 2 2 5z"/></svg>
        <span>info@warrendpellham-example.com</span>
      </li>
      <li>
        <svg viewBox="0 0 16 16" aria-hidden="true"><circle cx="8" cy="8" r="7"/><ellipse cx="8" cy="8" rx="3" ry="6.2" fill="none" stroke="#c3ae91" stroke-width="1.1"/><path d="M1.5 8h13M2.5 5h11M2.5 11h11" stroke="#c3ae91" stroke-width="1"/></svg>
        <span>www.warrendpellham-example.com</span>
      </li>
    </ul>
  </section>

</body>
</html>
```